Update existing icons for an admin interface to look more professional high end

Please see attached 4 files.
One from a competitor system which looks more high end and our icon files and how they look in the interface.
We need to suit to high end network administrators and need a more professional high end look. They need be in the same blueish color theme.

```html
<!DOCTYPE html>
<html lang="en">
<head>
<meta charset="utf-8">
<title>Admin Navigation</title>
<link href="https://fonts.googleapis.com/css2?family=Arimo:wght@400;700&display=swap" rel="stylesheet">
<style>
  :root {
    --row-top: #3b4045;
    --row-bottom: #2c3034;
    --row-line: #1b1d20;
    --row-highlight: #4a5056;
    --active-top: #4a5c6b;
    --active-bottom: #3c4b58;
    --label: #ececec;
    --icon-blue: #5aa0e6;
    --icon-light: #9cc8f2;
    --badge-bg: #1e2124;
    --badge-border: #6a7076;
    --badge-text: #ffffff;
    --edge: #c9ced3;
    --page: #ffffff;
  }
  html, body {
    margin: 0;
    padding: 0;
    width: 948px;
    height: 1200px;
    overflow: hidden;
    background: var(--page);
    font-family: "Arimo", Arial, sans-serif;
  }
  .side-nav {
    width: 943px;
    border-right: 3px solid var(--edge);
    margin: 0;
    padding: 0;
    list-style: none;
  }
  .nav-item {
    position: relative;
    height: 87.5px;
    box-sizing: border-box;
    display: flex;
    align-items: center;
    background: linear-gradient(var(--row-top), var(--row-bottom));
    border-top: 2px solid var(--row-highlight);
    border-bottom: 3px solid var(--row-line);
  }
  .nav-item.is-active {
    background: linear-gradient(var(--active-top), var(--active-bottom));
  }
  .nav-item.is-active::after {
    content: "";
    position: absolute;
    right: -3px;
    top: 50%;
    transform: translateY(-50%);
    border-style: solid;
    border-width: 20px 20px 20px 0;
    border-color: transparent var(--page) transparent transparent;
  }
  .nav-icon {
    width: 54px;
    height: 54px;
    margin-left: 26px;
    flex: none;
  }
  .nav-label {
    margin-left: 10px;
    color: var(--label);
    font-size: 29px;
    flex: 1;
    white-space: nowrap;
  }
  .is-active .nav-label { font-weight: 700; color: #ffffff; }
  .nav-badge {
    min-width: 70px;
    height: 42px;
    box-sizing: border-box;
    margin-right: 25px;
    border: 2px solid var(--badge-border);
    border-radius: 6px;
    background: var(--badge-bg);
    color: var(--badge-text);
    font-weight: 700;
    font-size: 26px;
    display: flex;
    align-items: center;
    justify-content: center;
  }
</style>
</head>
<body>
<ul class="side-nav">
  <li class="nav-item">
    <svg class="nav-icon" viewBox="0 0 24 24" fill="none" stroke="var(--icon-blue)" stroke-width="1.8"><rect x="2" y="3" width="20" height="13" rx="1"/><path d="M8 21h8M12 16v5"/></svg>
    <span class="nav-label">Home</span>
  </li>
  <li class="nav-item">
    <svg class="nav-icon" viewBox="0 0 24 24" fill="none" stroke="var(--icon-blue)" stroke-width="2" stroke-linecap="round"><circle cx="12" cy="12" r="10"/><circle cx="12" cy="12" r="5.5" stroke-width="1.5"/><path d="M12 12l6-6" stroke="var(--icon-light)"/><circle cx="12" cy="12" r="1.5" fill="var(--icon-light)" stroke="none"/></svg>
    <span class="nav-label">Vulnerability Scanner</span>
    <span class="nav-badge">10</span>
  </li>
  <li class="nav-item">
    <svg class="nav-icon" viewBox="0 0 24 24" fill="none" stroke="var(--icon-blue)" stroke-width="2"><circle cx="12" cy="12" r="10"/><path d="M12 6v6h-5" stroke="var(--icon-light)"/></svg>
    <span class="nav-label">Schedule</span>
    <span class="nav-badge">2</span>
  </li>
  <li class="nav-item">
    <svg class="nav-icon" viewBox="0 0 24 24" fill="none" stroke="var(--icon-blue)" stroke-width="1.8"><path d="M3 3v18h18"/><path d="M5 17l5-7 4 4 6-8" stroke="var(--icon-light)"/></svg>
    <span class="nav-label">Statistics</span>
    <span class="nav-badge">2</span>
  </li>
  <li class="nav-item">
    <svg class="nav-icon" viewBox="0 0 24 24" fill="none" stroke="var(--icon-blue)" stroke-width="1.6"><rect x="1" y="8" width="22" height="8"/><path d="M4 10v4M7 10v4M10 10v4M14 10v4M17 10v4M20 10v4"/></svg>
    <span class="nav-label">Tickets</span>
    <span class="nav-badge">3</span>
  </li>
  <li class="nav-item">
    <svg class="nav-icon" viewBox="0 0 24 24" fill="none" stroke="var(--icon-blue)" stroke-width="2" stroke-linecap="round"><path d="M2 9a14 14 0 0 1 20 0M5 12.5a9.5 9.5 0 0 1 14 0M8.5 16a4.5 4.5 0 0 1 7 0"/><circle cx="12" cy="19.5" r="1.4" fill="var(--icon-blue)"/></svg>
    <span class="nav-label">WiFi Pen Test</span>
    <span class="nav-badge">15</span>
  </li>
  <li class="nav-item">
    <svg class="nav-icon" viewBox="0 0 24 24" fill="var(--icon-blue)"><circle cx="12" cy="7" r="5"/><path d="M3 22c0-6 4-9 9-9s9 3 9 9z"/></svg>
    <span class="nav-label">Cloud Users</span>
    <span class="nav-badge">5</span>
  </li>
  <li class="nav-item is-active">
    <svg class="nav-icon" viewBox="0 0 24 24" fill="none" stroke="var(--icon-light)" stroke-width="1.8"><rect x="2" y="3" width="20" height="14"/><path d="M7 10h10M7 10l2.5-2.5M7 10l2.5 2.5M17 10l-2.5-2.5M17 10l-2.5 2.5M12 17v4M8 21h8"/></svg>
    <span class="nav-label">Scan Distribution</span>
  </li>
  <li class="nav-item">
    <svg class="nav-icon" viewBox="0 0 24 24" fill="var(--icon-blue)"><path d="M10 1h4l.6 3 2.4 1 2.6-1.7 2.8 2.8L20.7 8.7l1 2.4 3 .6v.6h-.7v3l-3 .6-1 2.4 1.7 2.6-2.8 2.8-2.6-1.7-2.4 1-.6 3h-4l-.6-3-2.4-1-2.6 1.7-2.8-2.8 1.7-2.6-1-2.4-3-.6v-4l3-.6 1-2.4L3.6 6.1l2.8-2.8L9 5l1-.4z"/><circle cx="12" cy="12" r="3.5" fill="var(--row-bottom)"/></svg>
    <span class="nav-label">System</span>
    <span class="nav-badge">19</span>
  </li>
  <li class="nav-item">
    <svg class="nav-icon" viewBox="0 0 24 24" fill="none" stroke="var(--icon-blue)" stroke-width="1.6"><rect x="2" y="2" width="8" height="6"/><rect x="14" y="2" width="8" height="6"/><rect x="8" y="16" width="8" height="6"/><path d="M6 8v4h12V8M12 12v4"/></svg>
    <span class="nav-label">Network Setup</span>
    <span class="nav-badge">4</span>
  </li>
  <li class="nav-item">
    <svg class="nav-icon" viewBox="0 0 24 24" fill="none" stroke="var(--icon-blue)" stroke-width="2.4"><path d="M4 11a8 8 0 0 1 14-5M20 13a8 8 0 0 1-14 5"/><path d="M19 2v5h-5M5 22v-5h5" stroke-width="2"/></svg>
    <span class="nav-label">Update</span>
    <span class="nav-badge">4</span>
  </li>
  <li class="nav-item">
    <svg class="nav-icon" viewBox="0 0 24 24" fill="none" stroke-width="4.5"><circle cx="12" cy="12" r="7.5" stroke="var(--icon-blue)"/><path d="M12 4.5a7.5 7.5 0 0 1 7.5 7.5M12 19.5a7.5 7.5 0 0 1-7.5-7.5" stroke="var(--icon-light)"/></svg>
    <span class="nav-label">Support</span>
    <span class="nav-badge">19</span>
  </li>
</ul>
</body>
</html>
```